App for Basket Haven to Link to Our Site and do simple things

After Simple design that acts as an interface for our customers. the app does simple things.

*Links to our Webpage - www.baskethaven.com.au
Shopping cart will live on our website

*People can call us from App - 1800 742 918
*People can send us a message from App
*We can Send Push Notifications
*Page dedicated to specials

*Link to Diary/Calendar (or create a inbuilt calendar) to remind people of upcoming birthdays/Anniversaries*** Reminder set 7 to 15 days before event to give enough time to send a gift.

Target Market(s)

People can download the app so they have our details handy on their phone

Industry/Entity Type

Retail

Colors

Designer to choose colors to be used in the design.

Requirements
Must have
• *** PREFER AN APP DESIGNER WHO CAN CODE THE APP AS WELL***
• Link to Diary/Calendar (or create a inbuilt calendar) to remind people of upcoming birthdays/Anniversaries*** Reminder set 7 to 15 days before event to give enough time to send a gift.
• Need to be able to send push notifications with special coupon codes
• Need to be able to send Push notifications
• Our Logo/as it or modified
• a map for directions 518 Tallowgate Road, West Brunswick VIC 3055
• Need to be able to change the Banner as needed

```html
<!DOCTYPE html>
<html lang="en">
<head>
<meta charset="utf-8">
<title>Basket Haven – Messages</title>
<link rel="stylesheet" href="https://fonts.googleapis.com/css2?family=Arimo:wght@400;500;700&display=swap">
<style>
  :root {
    --teal: #14bdd6;
    --teal-soft: #8fdbe8;
    --white: #ffffff;
    --ink: #4f5256;
    --muted: #b3b8c0;
    --divider: #e8eaec;
  }
  * { box-sizing: border-box; margin: 0; padding: 0; }
  html, body {
    width: 720px; height: 1200px; overflow: hidden;
    background: var(--white);
    font-family: "Arimo", Arial, sans-serif;
  }
  .screen { position: relative; width: 720px; height: 1200px; display: flex; flex-direction: column; }

  .status-bar {
    height: 36px; background: var(--teal); color: var(--white);
    display: flex; align-items: center; justify-content: space-between;
    padding: 4px 10px 0 10px; font-size: 21px; position: relative;
  }
  .status-left, .status-right { display: flex; align-items: center; gap: 8px; }
  .signal { letter-spacing: -1px; font-size: 16px; }
  .status-time { position: absolute; left: 50%; transform: translateX(-50%); top: 8px; }
  .battery { width: 44px; height: 18px; border: 2px solid var(--white); border-radius: 4px; padding: 2px; position: relative; }
  .battery::after { content: ""; position: absolute; right: -5px; top: 4px; width: 3px; height: 6px; background: var(--white); border-radius: 0 2px 2px 0; }
  .battery-level { width: 76%; height: 100%; background: var(--white); border-radius: 1px; }

  .app-header {
    height: 96px; background: var(--teal); color: var(--white);
    display: flex; align-items: center; justify-content: space-between; padding: 0 40px;
  }
  .app-title { font-size: 28px; font-weight: 500; }

  .content { flex: 1; display: flex; flex-direction: column; align-items: center; }
  .empty-illustration {
    margin-top: 180px; width: 370px; height: 300px; border-radius: 50%;
    background: radial-gradient(circle at center, var(--teal) 0%, var(--teal-soft) 45%, var(--white) 72%);
  }
  .empty-title { margin-top: 93px; font-size: 32px; line-height: 37px; color: var(--ink); font-weight: 500; }
  .send-button {
    margin-top: 165px; width: 423px; height: 80px; border: none;
    background: var(--teal); color: var(--white);
    font-family: inherit; font-size: 21px; letter-spacing: 0.3px;
    box-shadow: 0 3px 6px rgba(0,0,0,0.15); border-radius: 2px;
  }

  .tab-bar {
    height: 95px; border-top: 1px solid var(--divider);
    display: flex; background: var(--white);
  }
  .tab {
    flex: 1; display: flex; flex-direction: column; align-items: center; justify-content: center;
    gap: 6px; color: var(--muted); font-size: 20px; position: relative;
  }
  .tab svg { fill: var(--muted); }
  .tab.is-active { color: var(--teal); }
  .tab.is-active svg { fill: var(--teal); }
  .tab.is-active::after {
    content: ""; position: absolute; bottom: 0; left: 50%; transform: translateX(-50%);
    width: 118px; height: 4px; background: var(--teal);
  }
</style>
</head>
<body>
<div class="screen">
  <div class="status-bar">
    <div class="status-left">
      <span class="signal">●●●○○</span><span>ORBIT</span>
      <svg width="22" height="16" viewBox="0 0 22 16" fill="none" stroke="#fff" stroke-width="2.4" stroke-linecap="round"><path d="M2 5.5a13 13 0 0 1 18 0"/><path d="M5.5 9a8 8 0 0 1 11 0"/><circle cx="11" cy="13" r="1.6" fill="#fff" stroke="none"/></svg>
    </div>
    <span class="status-time">19:40</span>
    <div class="status-right">
      <svg width="14" height="22" viewBox="0 0 14 22" fill="none" stroke="#fff" stroke-width="1.8"><path d="M2 6l10 9-5 5V2l5 5-10 9"/></svg>
      <span>78%</span>
      <div class="battery"><div class="battery-level"></div></div>
    </div>
  </div>

  <header class="app-header">
    <svg width="38" height="30" viewBox="0 0 38 30" fill="none" stroke="#fff" stroke-width="3.4" stroke-linecap="round"><path d="M2 3h34M2 15h34M2 27h34"/></svg>
    <h1 class="app-title">Messages</h1>
    <svg width="36" height="36" viewBox="0 0 36 36" fill="none" stroke="#fff" stroke-width="3.4" stroke-linecap="round"><circle cx="14" cy="14" r="11"/><path d="M22 22l11 11"/></svg>
  </header>

  <main class="content">
    <div class="empty-illustration" role="img" aria-label="Empty inbox illustration: teal chat bubble with a zero count badge and scattered decorative dots"></div>
    <p class="empty-title">No Message, yet.</p>
    <button class="send-button">SEND MESSAGE</button>
  </main>

  <nav class="tab-bar">
    <div class="tab">
      <svg width="40" height="34" viewBox="0 0 40 34"><path d="M20 2L2 18h5v14h10v-9h6v9h10V18h5z"/></svg>
      <span>Home</span>
    </div>
    <div class="tab is-active">
      <svg width="42" height="34" viewBox="0 0 42 34"><rect x="1" y="2" width="40" height="30" rx="3"/><path d="M6 9l15 11 15-11" fill="none" stroke="#fff" stroke-width="3" stroke-linecap="round"/></svg>
      <span>Message</span>
    </div>
    <div class="tab">
      <svg width="52" height="36" viewBox="0 0 52 36"><path d="M2 2h48v32H2zM6 10v20h26V20H6zm30 0v20h10V10zM6 10h26v6H6z" fill-rule="evenodd"/></svg>
      <span>Web</span>
    </div>
    <div class="tab">
      <svg width="38" height="38" viewBox="0 0 38 38"><path d="M2 6h34v30H2zM6 14v18h26V14z" fill-rule="evenodd"/><rect x="9" y="1" width="4" height="9" rx="1"/><rect x="25" y="1" width="4" height="9" rx="1"/><rect x="11" y="20" width="4" height="4"/><rect x="17" y="20" width="4" height="4"/><rect x="23" y="20" width="4" height="4"/></svg>
      <span>Session</span>
    </div>
    <div class="tab">
      <svg width="42" height="38" viewBox="0 0 42 38"><circle cx="21" cy="10" r="9"/><path d="M2 36c0-10 8-15 19-15s19 5 19 15z"/></svg>
      <span>Profile</span>
    </div>
  </nav>
</div>
</body>
</html>
```